Lawn mowing business card design

We need a business card design for our lawn mowing and gardening business which is located in the Northern Beaches of Sydney. Our business name is Meadowline Turf and our logo is predominantly green and yellow in color. Please see our website at www.meadowlineturf.com.au for design ideas. The business targets young professionals and older clientele. As such the font should be easy to read, but I also want the business card to be colorful and stand out.

Target Market(s)

young professionals

Industry/Entity Type

Lawn Care

Contact Information for Business Card

Meadowline Turf, Gareth Pellow, 0478559201, www.meadowlineturf.com.au, email: meadowlineturf@mailbox-example.com

Font styles to use
Serif

Colors
9bcb3b
fbed22

Requirements
Must have
• Must include the details listed above. Must include the attached logo.
Nice to have
• Logo attached with two copies. The logo without any writing is high quality, please feel free to be creative with the text stating our business name "Meadowline Turf" using this file.

```html
<!DOCTYPE html>
<html lang="en">
<head>
<meta charset="utf-8">
<title>Meadowline Turf – Business Card</title>
<link href="https://fonts.googleapis.com/css2?family=Arvo:wght@400;700&display=swap" rel="stylesheet">
<style>
  :root {
    --bg: #e9e6e1;
    --card-white: #ffffff;
    --card-black: #111213;
    --brand-green: #2e8b3a;
    --brand-lime: #9bcb3b;
    --brand-yellow: #fbed22;
    --yellow-deep: #f2b705;
    --text-yellow: #f6c419;
    --text-light: #f4f4f4;
    --logo-ink: #1f6b2c;
  }
  * { box-sizing: border-box; margin: 0; padding: 0; }
  html, body { width: 1200px; height: 913px; overflow: hidden; }
  body {
    background: var(--bg);
    font-family: "Arvo", Georgia, serif;
    position: relative;
  }
  .card {
    position: absolute;
    width: 560px;
    height: 320px;
    border-radius: 22px;
    overflow: hidden;
    box-shadow: 0 10px 28px rgba(0,0,0,.18);
  }
  .card--front { left: 50px; top: 120px; background: var(--card-white); }
  .card--back {
    left: 590px; top: 470px;
    background: linear-gradient(160deg, var(--brand-yellow) 0%, #f7d51a 55%, var(--yellow-deep) 100%);
  }
  .card__art { position: absolute; inset: 0; width: 100%; height: 100%; }

  .brand {
    position: absolute;
    display: flex;
    align-items: center;
    gap: 10px;
  }
  .brand__mark {
    width: 22px; height: 22px;
    background: var(--brand-green);
    flex: none;
  }
  .brand__name {
    font-weight: 700;
    color: var(--logo-ink);
    white-space: nowrap;
  }
  .card--front .brand { left: 28px; top: 118px; }
  .card--front .brand__name { font-size: 18px; }
  .card--back .brand { left: 50%; top: 50%; transform: translate(-50%, -50%); gap: 14px; }
  .card--back .brand__mark { width: 38px; height: 38px; }
  .card--back .brand__name { font-size: 38px; }

  .contact {
    position: absolute;
    right: 26px;
    top: 72px;
    text-align: right;
    color: var(--text-yellow);
  }
  .contact__name { font-size: 22px; font-weight: 700; letter-spacing: .3px; }
  .contact__role { font-size: 12px; color: var(--text-light); margin-top: 2px; margin-bottom: 22px; }
  .contact__list { list-style: none; }
  .contact__item {
    display: flex; justify-content: flex-end; align-items: center; gap: 8px;
    font-size: 12px; line-height: 22px; white-space: nowrap;
  }
  .contact__icon { width: 12px; height: 12px; flex: none; }
</style>
</head>
<body>

<section class="card card--front">
  <svg class="card__art" viewBox="0 0 560 320" preserveAspectRatio="none" aria-hidden="true">
    <path d="M330,0 C230,40 260,170 160,250 C120,285 70,305 10,320 L560,320 L560,0 Z" fill="var(--brand-lime)"/>
    <path d="M345,0 C245,40 275,170 175,250 C135,285 85,305 25,320 L560,320 L560,0 Z" fill="var(--card-white)"/>
    <path d="M360,0 C260,40 290,170 190,250 C150,285 100,305 40,320 L560,320 L560,0 Z" fill="var(--card-black)"/>
    <path d="M0,304 C45,310 95,302 140,284" stroke="var(--brand-green)" stroke-width="6" fill="none"/>
  </svg>

  <div class="brand">
    <span class="brand__mark"></span>
    <span class="brand__name">Meadowline Turf</span>
  </div>

  <div class="contact">
    <p class="contact__name">Gareth Pellow</p>
    <p class="contact__role">Director</p>
    <ul class="contact__list">
      <li class="contact__item">0478559201
        <svg class="contact__icon" viewBox="0 0 12 12"><path d="M3 1 L5 3 L4 5 Q5 7 7 8 L9 7 L11 9 L9 11 Q2 10 1 3 Z" fill="var(--text-light)"/></svg>
      </li>
      <li class="contact__item">meadowlineturf@mailbox-example.com
        <svg class="contact__icon" viewBox="0 0 12 12"><rect x="1" y="2.5" width="10" height="7" fill="none" stroke="var(--text-light)" stroke-width="1.2"/><path d="M1 3 L6 7 L11 3" fill="none" stroke="var(--text-light)" stroke-width="1.2"/></svg>
      </li>
      <li class="contact__item">www.meadowlineturf.com.au
        <svg class="contact__icon" viewBox="0 0 12 12"><circle cx="6" cy="6" r="5" fill="none" stroke="var(--text-light)" stroke-width="1.2"/><path d="M1 6 H11 M6 1 Q3 6 6 11 M6 1 Q9 6 6 11" fill="none" stroke="var(--text-light)" stroke-width="1"/></svg>
      </li>
    </ul>
  </div>
</section>

<section class="card card--back">
  <div class="brand">
    <span class="brand__mark"></span>
    <span class="brand__name">Meadowline Turf</span>
  </div>
</section>

</body>
</html>
```